Pain Management, Personal Injury & Motor Vehicle Accident

I need t rack card to use as marketing collateral while talking to urgent cares, wreckers services, primary care, and emergency room staff
If you have been involved in a motor vehicle accident or personal injury accident, Prairie Ridge Relief Clinic is your Solution to complete pain relief. We understand your pain and are here to assist you along the journey to becoming pain free. It is crucial that you choose a physician who is experienced in treating your unique injury.
At Prairie Ridge Relief Clinic, Dr Colin Marsh and his team of experts will provide you with a specialized approach to reducing and managing your pain with a comprehensive and effective treatment plan based on a proper diagnosis. You can expect an exceptional treatment program for your injuries to help you to begin improving your quality of life immediately.
We treat:
Car Accident Injuries
Semi Truck Injuries
Most Personal Injuries
Slip and Falls
Motorcycle Accident Injuries
Whiplash
Back Injuries
Neck Injuries
Shoulder Injuries
Headaches
Locations: Cedar Bend, Larkfield, Stonemoor
Phone: (580) 472-6193
Fax: (833) 718-2947
www.prairieridgerelief.example
Target Market(s)
Urgent Cares, Emergency Rooms, Primary Care, Wrecker Services, anyone involved in a Personal Injury or Motor Vehicle Accident
Industry/Entity Type
Healthcare, Motor Vehicle Accident Injury, Personal Injury, Pain Management, Pain Relief

```html
<!DOCTYPE html>
<html lang="en">
<head>
<meta charset="utf-8">
<title>Prairie Ridge Relief Clinic – Rack Card</title>
<link href="https://fonts.googleapis.com/css2?family=Montserrat:wght@400;500;600;700;800&display=swap" rel="stylesheet">
<style>
  :root{
    --red:#d42129;
    --ink:#1d1d1b;
    --text:#2b2b2b;
    --page:#efefef;
    --white:#ffffff;
  }
  *{box-sizing:border-box;margin:0;padding:0}
  html,body{width:783px;height:1200px;overflow:hidden;background:var(--page);font-family:"Montserrat",sans-serif;color:var(--text)}
  .card{position:absolute;left:31px;width:720px;height:514px;background:var(--white);overflow:hidden;box-shadow:0 2px 8px rgba(0,0,0,.12)}
  .card--front{top:40px}
  .card--back{top:620px}
  .layer{position:absolute;inset:0}
  .photo{position:absolute}
  .front-photo{left:330px;top:0;width:390px;height:470px;
    background:linear-gradient(90deg,rgba(255,255,255,1) 0%,rgba(255,255,255,0) 30%),
      linear-gradient(180deg,#e4e6e8 0%,#d9dcdf 35%,#e7c3b3 65%,#efd3c6 100%)}
  .brand{position:absolute;left:42px;top:56px;display:flex;align-items:center;gap:8px}
  .brand-dot{width:18px;height:18px;border-radius:50%;background:var(--red)}
  .brand-name{font-size:11px;font-weight:600;color:var(--ink)}
  .title{position:absolute;left:40px;top:112px;line-height:1}
  .title-top{display:block;font-size:31px;font-weight:800;color:var(--ink);letter-spacing:-.5px}
  .title-main{display:block;font-size:39px;font-weight:800;color:var(--red);letter-spacing:-.8px;margin-top:3px}
  .rule{position:absolute;left:40px;top:199px;width:329px;height:1px;background:#bdbdbd}
  .rule::before{content:"";position:absolute;left:18px;top:-2px;width:44px;height:5px;border-radius:3px;background:var(--ink)}
  .lead{position:absolute;left:41px;top:217px;width:340px;font-size:11.3px;font-weight:500;line-height:1.23;color:var(--ink)}
  .contacts{position:absolute;left:52px;top:376px;list-style:none}
  .contacts li{display:flex;align-items:center;height:29px;color:var(--white);font-weight:600;font-size:19px;letter-spacing:.2px}
  .contacts li.small{height:27px;font-size:18px}
  .contacts svg{width:16px;height:16px;margin-right:10px;flex:none}

  .about{position:absolute;left:36px;top:32px;width:336px}
  .heading{font-size:13.5px;font-weight:500;color:var(--ink);letter-spacing:.2px}
  .heading b{color:var(--red);font-weight:700}
  .about p{font-size:7.4px;line-height:1.38;text-align:justify;margin-top:7px;color:#3a3a3a}
  .about p + p{margin-top:8px}
  .treat{position:absolute;left:36px;top:189px}
  .services{position:absolute;left:36px;top:308px}
  .ticks{list-style:none;margin-top:10px}
  .ticks--cols{display:grid;grid-template-columns:174px 120px;row-gap:5.5px}
  .ticks--single li{margin-bottom:5.5px}
  .ticks li{display:flex;align-items:center;font-size:7.4px;font-weight:600;color:var(--ink);height:10.5px}
  .tick-icon{display:inline-block;width:8px;height:8px;margin-right:8px;flex:none}
  .back-contacts{position:absolute;left:0;top:432px;width:720px;color:var(--white);font-weight:600}
  .back-contacts .row{position:absolute;display:flex;align-items:center;font-size:13.5px;white-space:nowrap}
  .back-contacts svg{width:12px;height:12px;margin-right:6px;flex:none}
</style>
</head>
<body>

<section class="card card--front">
  <div class="photo front-photo" role="img" aria-label="Photo of a clinician examining an older woman's neck and shoulder in a clinic office"></div>

  <svg class="layer" width="720" height="514" viewBox="0 0 720 514">
    <path d="M0,285 C70,250 160,262 235,300" fill="none" stroke="var(--ink)" stroke-width="8"/>
    <path d="M0,302 C80,266 170,280 245,318 C335,368 430,420 525,446 C610,468 665,448 720,432 L720,514 L0,514 Z" fill="var(--red)"/>
    <path d="M165,322 C230,300 290,300 350,330 C430,370 500,420 580,458 C630,480 680,478 720,455"
      fill="none" stroke="var(--ink)" stroke-width="28" stroke-linecap="round" role="img" aria-label="Spine vertebrae illustration"/>
  </svg>

  <div class="brand"><span class="brand-dot"></span><span class="brand-name">Prairie Ridge Relief Clinic</span></div>

  <h1 class="title"><span class="title-top">PRAIRIE RIDGE</span><span class="title-main">RELIEF CLINIC</span></h1>
  <div class="rule"></div>
  <p class="lead">If you have been involved in a motor vehicle accident or personal injury accident, Prairie Ridge Relief Clinic is your Solution to complete pain relief.</p>

  <ul class="contacts">
    <li><svg viewBox="0 0 16 16"><path d="M3.5 1.5l2.5 .5 1 3-1.8 1.3a9 9 0 0 0 4.5 4.5L11 9l3 1 .5 2.5-1.8 1.8C7.5 14 2 8.5 1.7 3.3z" fill="none" stroke="#fff" stroke-width="1.4" stroke-linejoin="round"/></svg>(580) 472-6193</li>
    <li><svg viewBox="0 0 16 16"><rect x="4" y="1.5" width="8" height="4" fill="#fff"/><rect x="1" y="6" width="14" height="6" rx="1" fill="#fff"/><rect x="4" y="10" width="8" height="5" fill="#fff" stroke="var(--red)" stroke-width="1"/></svg>(833) 718-2947</li>
    <li><svg viewBox="0 0 16 16"><path d="M8 15s-5-5.5-5-9a5 5 0 0 1 10 0c0 3.5-5 9-5 9z" fill="#fff"/><circle cx="8" cy="6" r="2" fill="var(--red)"/></svg>Cedar Bend, Larkfield, Stonemoor</li>
    <li class="small"><svg viewBox="0 0 16 16"><g fill="none" stroke="#fff" stroke-width="1.2"><circle cx="8" cy="8" r="6.5"/><ellipse cx="8" cy="8" rx="3" ry="6.5"/><path d="M1.5 8h13M2.5 5h11M2.5 11h11"/></g></svg>www.prairieridgerelief.example</li>
  </ul>
</section>

<section class="card card--back">
  <svg class="layer" width="720" height="514" viewBox="0 0 720 514">
    <defs>
      <linearGradient id="backPhoto" x1="0" y1="0" x2="0" y2="1">
        <stop offset="0" stop-color="#dcdcdc"/>
        <stop offset=".5" stop-color="#cfcfcf"/>
        <stop offset=".7" stop-color="#e2a6a6"/>
        <stop offset="1" stop-color="#d6d6d6"/>
      </linearGradient>
      <linearGradient id="softPhoto" x1="0" y1="0" x2="1" y2="0">
        <stop offset="0" stop-color="#fff" stop-opacity="0"/>
        <stop offset=".6" stop-color="#e4e4e4"/>
        <stop offset="1" stop-color="#fff" stop-opacity="0"/>
      </linearGradient>
      <linearGradient id="doctor" x1="0" y1="0" x2="0" y2="1">
        <stop offset="0" stop-color="#5d6670"/>
        <stop offset=".55" stop-color="#8d7a6c"/>
        <stop offset="1" stop-color="#f4f4f4"/>
      </linearGradient>
    </defs>
    <rect x="175" y="300" width="215" height="110" fill="url(#softPhoto)" role="img" aria-label="Soft faded photo of a back massage treatment"/>
    <path d="M478,0 C385,110 375,330 505,452 L720,452 L720,0 Z" fill="url(#backPhoto)" role="img" aria-label="Photo of a person holding their lower back in pain"/>
    <path d="M468,0 C372,110 362,330 495,452" fill="none" stroke="var(--ink)" stroke-width="7"/>
    <path d="M0,412 C70,436 150,438 230,420" fill="none" stroke="var(--ink)" stroke-width="9"/>
    <path d="M0,447 C120,450 230,418 340,410 C460,402 570,448 720,440 L720,514 L0,514 Z" fill="var(--red)"/>
    <circle cx="439" cy="357" r="78" fill="none" stroke="#c8c8c8" stroke-width="1"/>
    <circle cx="439" cy="357" r="72" fill="var(--white)"/>
    <circle cx="439" cy="357" r="66" fill="url(#doctor)" role="img" aria-label="Portrait of Dr Colin Marsh in a white coat"/>
    <g fill="#b5b5b5"><circle cx="358" cy="345" r="5"/><circle cx="356" cy="362" r="4.5"/><circle cx="358" cy="378" r="4"/><circle cx="362" cy="392" r="3"/><circle cx="368" cy="404" r="2.5"/><circle cx="376" cy="414" r="2"/></g>
  </svg>

  <div class="about">
    <h2 class="heading">ABOUT <b>US</b></h2>
    <p>If you have been involved in a motor vehicle accident or personal injury accident, Prairie Ridge Relief Clinic is your Solution to complete pain relief. We understand your pain and are here to assist you along the journey to becoming pain free. It is crucial that you choose a physician who is experienced in treating your unique injury.</p>
    <p>At Prairie Ridge Relief Clinic, Dr Colin Marsh and his team of experts will provide you with a specialized approach to reducing and managing your pain with a comprehensive and effective treatment plan based on a proper diagnosis. You can expect an exceptional treatment program for your injuries to help you to begin improving your quality of life immediately.</p>
  </div>

  <div class="treat">
    <h2 class="heading">WE <b>TREAT</b></h2>
    <ul class="ticks ticks--cols">
      <li><svg class="tick-icon" viewBox="0 0 8 8"><circle cx="4" cy="4" r="4" fill="var(--red)"/><path d="M2.2 4.1l1.2 1.2 2.4-2.5" fill="none" stroke="#fff" stroke-width="1"/></svg>Car Accident Injuries</li>
      <li><svg class="tick-icon" viewBox="0 0 8 8"><circle cx="4" cy="4" r="4" fill="var(--red)"/><path d="M2.2 4.1l1.2 1.2 2.4-2.5" fill="none" stroke="#fff" stroke-width="1"/></svg>Whiplash</li>
      <li><svg class="tick-icon" viewBox="0 0 8 8"><circle cx="4" cy="4" r="4" fill="var(--red)"/><path d="M2.2 4.1l1.2 1.2 2.4-2.5" fill="none" stroke="#fff" stroke-width="1"/></svg>Semi Truck Injuries</li>
      <li><svg class="tick-icon" viewBox="0 0 8 8"><circle cx="4" cy="4" r="4" fill="var(--red)"/><path d="M2.2 4.1l1.2 1.2 2.4-2.5" fill="none" stroke="#fff" stroke-width="1"/></svg>Back Injuries</li>
      <li><svg class="tick-icon" viewBox="0 0 8 8"><circle cx="4" cy="4" r="4" fill="var(--red)"/><path d="M2.2 4.1l1.2 1.2 2.4-2.5" fill="none" stroke="#fff" stroke-width="1"/></svg>Most Personal Injuries</li>
      <li><svg class="tick-icon" viewBox="0 0 8 8"><circle cx="4" cy="4" r="4" fill="var(--red)"/><path d="M2.2 4.1l1.2 1.2 2.4-2.5" fill="none" stroke="#fff" stroke-width="1"/></svg>Neck Injuries</li>
      <li><svg class="tick-icon" viewBox="0 0 8 8"><circle cx="4" cy="4" r="4" fill="var(--red)"/><path d="M2.2 4.1l1.2 1.2 2.4-2.5" fill="none" stroke="#fff" stroke-width="1"/></svg>Slip and Falls</li>
      <li><svg class="tick-icon" viewBox="0 0 8 8"><circle cx="4" cy="4" r="4" fill="var(--red)"/><path d="M2.2 4.1l1.2 1.2 2.4-2.5" fill="none" stroke="#fff" stroke-width="1"/></svg>Shoulder Injuries</li>
      <li><svg class="tick-icon" viewBox="0 0 8 8"><circle cx="4" cy="4" r="4" fill="var(--red)"/><path d="M2.2 4.1l1.2 1.2 2.4-2.5" fill="none" stroke="#fff" stroke-width="1"/></svg>Motorcycle Accident Injuries</li>
      <li><svg class="tick-icon" viewBox="0 0 8 8"><circle cx="4" cy="4" r="4" fill="var(--red)"/><path d="M2.2 4.1l1.2 1.2 2.4-2.5" fill="none" stroke="#fff" stroke-width="1"/></svg>Headaches</li>
    </ul>
  </div>

  <div class="services">
    <h2 class="heading">TREATMENT <b>SERVICES</b></h2>
    <ul class="ticks ticks--single">
      <li><svg class="tick-icon" viewBox="0 0 8 8"><circle cx="4" cy="4" r="4" fill="var(--red)"/><path d="M2.2 4.1l1.2 1.2 2.4-2.5" fill="none" stroke="#fff" stroke-width="1"/></svg>Pain Managememnt</li>
      <li><svg class="tick-icon" viewBox="0 0 8 8"><circle cx="4" cy="4" r="4" fill="var(--red)"/><path d="M2.2 4.1l1.2 1.2 2.4-2.5" fill="none" stroke="#fff" stroke-width="1"/></svg>Nurological Evalutions</li>
      <li><svg class="tick-icon" viewBox="0 0 8 8"><circle cx="4" cy="4" r="4" fill="var(--red)"/><path d="M2.2 4.1l1.2 1.2 2.4-2.5" fill="none" stroke="#fff" stroke-width="1"/></svg>Orthopedic Evalutions</li>
      <li><svg class="tick-icon" viewBox="0 0 8 8"><circle cx="4" cy="4" r="4" fill="var(--red)"/><path d="M2.2 4.1l1.2 1.2 2.4-2.5" fill="none" stroke="#fff" stroke-width="1"/></svg>Orthopedic Surgical Interventions</li>
    </ul>
  </div>

  <div class="back-contacts">
    <div class="row" style="left:198px;top:4px"><svg viewBox="0 0 16 16"><rect x="4" y="1.5" width="8" height="4" fill="#fff"/><rect x="1" y="6" width="14" height="6" rx="1" fill="#fff"/><rect x="4" y="10" width="8" height="5" fill="#fff" stroke="var(--red)" stroke-width="1"/></svg>(833) 718-2947</div>
    <div class="row" style="left:32px;top:31px"><svg viewBox="0 0 16 16"><path d="M3.5 1.5l2.5 .5 1 3-1.8 1.3a9 9 0 0 0 4.5 4.5L11 9l3 1 .5 2.5-1.8 1.8C7.5 14 2 8.5 1.7 3.3z" fill="none" stroke="#fff" stroke-width="1.4" stroke-linejoin="round"/></svg>(580) 472-6193</div>
    <div class="row" style="left:198px;top:31px"><svg viewBox="0 0 16 16"><path d="M8 15s-5-5.5-5-9a5 5 0 0 1 10 0c0 3.5-5 9-5 9z" fill="#fff"/><circle cx="8" cy="6" r="2" fill="var(--red)"/></svg>Cedar Bend, Larkfield, Stonemoor</div>
    <div class="row" style="left:472px;top:31px;font-size:12.5px"><svg viewBox="0 0 16 16"><g fill="none" stroke="#fff" stroke-width="1.2"><circle cx="8" cy="8" r="6.5"/><ellipse cx="8" cy="8" rx="3" ry="6.5"/><path d="M1.5 8h13M2.5 5h11M2.5 11h11"/></g></svg>www.prairieridgerelief.example</div>
  </div>
</section>

</body>
</html>
```